Business Card Design

We would like a business card that utilizes our current logo and keeps with the same feel - elegant and organic. Our farm isn't about mass production, it's about excellence, education, beautiful events and flowers - people, culture, and community.

Target Market(s)

Patrons to our farm who are interested in weddings, events, or our flowers and vegetables.

Contact Information for Business Card

Name, address, cell email (Danielle Hoskins, 2716 Wrenfield Rd, Alder Bend, CO 80516, cell 30.412.6638, email danielle@wrenfieldacres.com)

```html
<!DOCTYPE html>
<html lang="en">
<head>
<meta charset="utf-8">
<title>Wrenfield Acres — Business Card</title>
<link rel="stylesheet" href="https://fonts.googleapis.com/css2?family=Playfair+Display:wght@500&family=Montserrat:wght@400&display=swap">
<style>
  :root {
    --page: #e9e9e6;
    --sage: #7b917d;
    --sage-deep: #6f8672;
    --paper: #ffffff;
    --bronze: #8b6a3e;
    --ink: #4a4a4a;
    --leaf: #7a9580;
  }
  * { box-sizing: border-box; margin: 0; padding: 0; }
  html, body { width: 1200px; height: 960px; overflow: hidden; }
  body {
    background: var(--page);
    display: flex;
    flex-direction: column;
    align-items: center;
    justify-content: center;
    gap: 60px;
  }
  .card {
    width: 700px;
    height: 400px;
    background: var(--paper);
    position: relative;
    overflow: hidden;
    box-shadow: 0 6px 18px rgba(0,0,0,0.12);
  }
  .pattern-band {
    position: absolute;
    left: 0;
    width: 100%;
    background: linear-gradient(180deg, var(--sage), var(--sage-deep));
  }

  /* Front */
  .card-front .pattern-band { top: 0; height: 150px; }
  .card-front .rule {
    position: absolute; top: 150px; left: 0; width: 100%; height: 8px;
    background: var(--bronze);
  }
  .card-front .wordmark {
    position: absolute; top: 36px; right: 44px;
    text-align: right;
    font-family: "Playfair Display", serif;
    font-weight: 500;
    color: var(--paper);
    line-height: 1;
  }
  .wordmark .wordmark-name { font-size: 38px; display: block; }
  .wordmark .wordmark-sub { font-size: 13px; letter-spacing: 0.55em; display: block; margin-top: 10px; }

  .contact { position: absolute; left: 56px; top: 196px; }
  .contact-name {
    font-family: "Playfair Display", serif;
    font-weight: 500;
    font-size: 31px;
    letter-spacing: 0.04em;
    text-transform: uppercase;
    color: var(--bronze);
    margin-bottom: 18px;
  }
  .contact-list { list-style: none; }
  .contact-list li {
    display: flex; align-items: center; gap: 14px;
    font-family: "Montserrat", sans-serif;
    font-size: 16px;
    color: var(--ink);
    height: 36px;
  }
  .contact-list svg { width: 18px; height: 18px; flex: none; }

  /* Back */
  .card-back .band-top { top: 0; height: 115px; }
  .card-back .band-bottom { bottom: 0; height: 115px; }
  .card-back .wordmark {
    position: absolute; top: 115px; left: 0; width: 100%; height: 170px;
    display: flex; flex-direction: column; align-items: center; justify-content: center;
    font-family: "Playfair Display", serif;
    font-weight: 500;
    color: var(--leaf);
    line-height: 1;
  }
  .card-back .wordmark .wordmark-name { font-size: 46px; }
  .card-back .wordmark .wordmark-sub { font-size: 14px; margin-top: 12px; padding-left: 0.55em; }
</style>
</head>
<body>

  <section class="card card-front">
    <div class="pattern-band" role="img" aria-label="Sage green band with a soft repeating four-petal flower pattern"></div>
    <div class="rule"></div>
    <div class="wordmark">
      <span class="wordmark-name">Wrenfield</span>
      <span class="wordmark-sub">ACRES</span>
    </div>
    <div class="contact">
      <h1 class="contact-name">Danielle Hoskins</h1>
      <ul class="contact-list">
        <li>
          <svg viewBox="0 0 18 18" aria-hidden="true"><path d="M9 1.5a5.5 5.5 0 0 0-5.5 5.5c0 4 5.5 9.5 5.5 9.5s5.5-5.5 5.5-9.5A5.5 5.5 0 0 0 9 1.5z" fill="var(--leaf)"/><circle cx="9" cy="7" r="2" fill="#fff"/></svg>
          2716 Wrenfield Rd, Alder Bend, CO 80516
        </li>
        <li>
          <svg viewBox="0 0 18 18" aria-hidden="true"><rect x="1.5" y="3.5" width="15" height="11" fill="none" stroke="var(--leaf)" stroke-width="1.6"/><path d="M1.5 3.5 9 10l7.5-6.5M1.5 14.5 7 9m9.5 5.5L11 9" fill="none" stroke="var(--leaf)" stroke-width="1.4"/></svg>
          danielle@wrenfieldacres.com
        </li>
        <li>
          <svg viewBox="0 0 18 18" aria-hidden="true"><rect x="2" y="2" width="14" height="14" rx="2.5" fill="none" stroke="var(--leaf)" stroke-width="1.6"/><g fill="var(--leaf)"><rect x="5" y="5" width="2.4" height="2.4"/><rect x="10.6" y="5" width="2.4" height="2.4"/><rect x="5" y="10.6" width="2.4" height="2.4"/><rect x="10.6" y="10.6" width="2.4" height="2.4"/></g></svg>
          30.412.6638
        </li>
      </ul>
    </div>
  </section>

  <section class="card card-back">
    <div class="pattern-band band-top" role="img" aria-label="Sage green band with a soft repeating four-petal flower pattern"></div>
    <div class="wordmark">
      <span class="wordmark-name">Wrenfield</span>
      <span class="wordmark-sub" style="letter-spacing:0.55em">ACRES</span>
    </div>
    <div class="pattern-band band-bottom" role="img" aria-label="Sage green band with a soft repeating four-petal flower pattern"></div>
  </section>

</body>
</html>
```